Trade Show Design

Two, doublesided backdrops/one doublesided banner/one countertop. I have 3 sample pictures of the 3 items that we are purchasing and all the dimensions are listed on the file names.
website: www.fixwiseworkshop-example.com
We are a training center that teaches homeowner's how to do their own home renovations through in-person classes with hands-on training.
We are looking to update our tradeshow displays utilizing stock photos as our photos do not have high enough resolution. I have attached lots of example pictures to select from but some of my favourites that I want to use are over 10 MB so they won't upload. Will have to figure out a different way to upload. Our tagline is build every room with confidence. We also use words such as "learn to reno" or "practical, hands-on training". We want to use our current branding (pictures of our minivan are uploaded as well) and our color palette document and really show people what we are all about - classes that people can attend so they can learn to reno their home.
Updates

For the 2 backdrops, we would like them to either be stand-alone or together incase we go to a trade show and only have room for 1 of them. They are to be different designs, front and back but a continuous flow if we are to use them together. Again, I have to figure out how to upload additional pictures as some of the ones I want to use are larger. Thanks!

Same with the Banner that is also double-sided - this is to be a different design for the back and front. We want minimal wording on everything but we really want to showcase what we do so that people can figure it out quickly when they walk by our booth....we offer in-person class with hands-on training. Learn to do by doing. Like on our vehicle that I sent example pictures of, we can put a list of a few topics so that people can understand:
Renovation Topics:
Bathroom
Drywall
Flooring
Tiling
Basement
Framing
Plumbing
Baseboards
Feature Walls

Here is the link to the Filebarn Vault to additional photos.

https://files.example-share.net/folders/7KX2b_pq9T-ZR4mNwEeLsUd8YtVaBcHqJ?usp=sharing

Thanks,
Marla

```html
<!DOCTYPE html>
<html lang="en">
<head>
<meta charset="utf-8">
<title>FixWise Workshop – Trade Show Backdrops</title>
<link rel="stylesheet" href="https://fonts.googleapis.com/css2?family=Exo+2:wght@400;700;800&display=swap">
<style>
  :root{
    --teal:#0f5e63;
    --gold:#cf9339;
    --olive:#c7c59c;
    --sky:#a8c0dc;
    --paper:#f3f3f2;
    --page:#ffffff;
    --grey:#5b6466;
  }
  *{margin:0;padding:0;box-sizing:border-box}
  html,body{width:1200px;height:483px;overflow:hidden;background:var(--page)}
  body{position:relative;font-family:"Exo 2",sans-serif}
  .backdrop{position:absolute;top:10px;width:581px;height:464px;background:var(--paper);overflow:hidden}
  .backdrop--front{left:11px}
  .backdrop--back{left:609px}
  .backdrop svg.art{position:absolute;inset:0;width:581px;height:464px}
  .brand{position:absolute;top:28px;display:flex;gap:7px;align-items:flex-start}
  .brand__mark{width:30px;height:30px;border:3px solid var(--teal);flex:none}
  .brand__name{font-weight:800;font-size:16px;line-height:1;color:var(--teal);text-transform:uppercase;letter-spacing:.3px;white-space:nowrap}
  .brand__tag{font-weight:400;font-size:8.5px;color:var(--grey);margin-top:5px;white-space:nowrap}
  .headline{position:absolute;font-weight:800;font-size:35px;line-height:1;color:var(--teal);letter-spacing:.3px;white-space:nowrap}
  .subhead{position:absolute;font-weight:800;color:var(--gold);line-height:1;text-transform:uppercase;white-space:nowrap}
  .topic{position:absolute;display:flex;align-items:center;gap:6px;font-weight:800;font-size:14.5px;color:var(--teal);text-transform:uppercase;letter-spacing:.4px;white-space:nowrap}
  .topic svg{width:14px;height:14px;flex:none}
  .web{position:absolute;height:18px;background:var(--gold);color:#fff;font-weight:800;font-size:9.5px;line-height:18px;white-space:nowrap;text-transform:uppercase;letter-spacing:0;padding:0 6px}
</style>
</head>
<body>

<section class="backdrop backdrop--front">
  <svg class="art" viewBox="0 0 900 720" preserveAspectRatio="none">
    <defs>
      <linearGradient id="warm" x1="0" y1="0" x2="1" y2="1"><stop offset="0" stop-color="#d9c3a6"/><stop offset="1" stop-color="#8a6a4e"/></linearGradient>
      <linearGradient id="cool" x1="0" y1="0" x2="1" y2="1"><stop offset="0" stop-color="#e7e3de"/><stop offset="1" stop-color="#9a8c80"/></linearGradient>
      <linearGradient id="red" x1="0" y1="0" x2="1" y2="1"><stop offset="0" stop-color="#e9e4dc"/><stop offset="1" stop-color="#a8483c"/></linearGradient>
    </defs>
    <polygon points="0,190 170,380 0,720" fill="var(--olive)"/>
    <polygon points="0,720 120,720 260,600 180,560" fill="var(--gold)"/>
    <polygon points="150,300 240,210 330,300 240,390" fill="var(--sky)"/>
    <polygon points="-22,310 103,185 223,310 103,435" fill="url(#red)" stroke="var(--gold)" stroke-width="4" role="img" aria-label="Photo: couple installing a ceiling light fixture"/>
    <polygon points="-22,455 38,350 98,440 38,530" fill="url(#warm)" stroke="var(--gold)" stroke-width="4" role="img" aria-label="Photo: hand marking wood with a pencil"/>
    <polygon points="73,500 248,330 423,500 248,675" fill="url(#warm)" stroke="var(--gold)" stroke-width="5" role="img" aria-label="Photo: student measuring a board with a tape measure"/>
    <polygon points="241,285 378,148 513,285 378,420" fill="url(#cool)" stroke="var(--teal)" stroke-width="4" role="img" aria-label="Photo: woman carrying a hammer and lumber"/>
    <polygon points="383,440 493,330 583,440 493,550" fill="url(#cool)" stroke="var(--teal)" stroke-width="4" role="img" aria-label="Photo: two students with tool belts and lumber"/>
    <polygon points="563,445 673,340 778,445 673,555" fill="url(#red)" stroke="var(--teal)" stroke-width="4" role="img" aria-label="Photo: students working on a flooring project"/>
  </svg>

  <div class="brand" style="left:34px">
    <span class="brand__mark"></span>
    <div><div class="brand__name">FixWise Workshop</div><div class="brand__tag">Build every room with confidence.</div></div>
  </div>

  <h1 class="headline" style="right:31px;top:62px">LEARN TO RENO</h1>
  <p class="subhead" style="right:31px;top:100px;font-size:16px">Practical, in-person classes</p>

  <div class="topic" style="left:336px;top:148px"><svg viewBox="0 0 14 14"><rect x="1" y="1" width="12" height="12" fill="none" stroke="var(--gold)" stroke-width="1.6"/><path d="M3 8h8M5 4v4" stroke="var(--gold)" stroke-width="1.4"/></svg>Bathroom</div>
  <div class="topic" style="left:457px;top:146px"><svg viewBox="0 0 14 14"><rect x="1" y="1" width="12" height="12" fill="none" stroke="var(--gold)" stroke-width="1.6"/><path d="M4 3v8M7 3v8M10 3v8" stroke="var(--gold)" stroke-width="1.2"/></svg>Drywall</div>
  <div class="topic" style="left:339px;top:169px"><svg viewBox="0 0 14 14"><path d="M7 1l6 4-6 4-6-4z M1 8l6 4 6-4" fill="none" stroke="var(--gold)" stroke-width="1.5"/></svg>Flooring</div>
  <div class="topic" style="left:452px;top:167px"><svg viewBox="0 0 14 14"><path d="M7 1l6 6-6 6-6-6z M4 4l6 6M10 4l-6 6" fill="none" stroke="var(--gold)" stroke-width="1.4"/></svg>Tiling</div>
  <div class="topic" style="left:392px;top:194px"><svg viewBox="0 0 14 14"><rect x="1" y="1" width="12" height="12" fill="none" stroke="var(--gold)" stroke-width="1.6"/><path d="M3 11l4-4 4 4M5 5h4" fill="none" stroke="var(--gold)" stroke-width="1.4"/></svg>Basement</div>

  <div class="web" style="left:329px;top:372px">www.fixwiseworkshop-example.com</div>
</section>

<section class="backdrop backdrop--back">
  <svg class="art" viewBox="0 0 900 720" preserveAspectRatio="none">
    <defs>
      <linearGradient id="warmB" x1="0" y1="0" x2="1" y2="1"><stop offset="0" stop-color="#d8c0a0"/><stop offset="1" stop-color="#7c5f48"/></linearGradient>
      <linearGradient id="coolB" x1="0" y1="0" x2="1" y2="1"><stop offset="0" stop-color="#ebe8e3"/><stop offset="1" stop-color="#8f9aa6"/></linearGradient>
      <linearGradient id="plaid" x1="0" y1="0" x2="1" y2="1"><stop offset="0" stop-color="#eae6e0"/><stop offset="1" stop-color="#3f6d8a"/></linearGradient>
    </defs>
    <polygon points="900,180 730,370 900,720" fill="var(--olive)"/>
    <polygon points="900,720 780,720 640,600 720,560" fill="var(--gold)"/>
    <polygon points="590,300 683,210 776,300 683,390" fill="var(--sky)"/>
    <polygon points="386,285 523,148 661,285 523,420" fill="url(#coolB)" stroke="var(--teal)" stroke-width="4" role="img" aria-label="Photo: smiling couple holding a power drill"/>
    <polygon points="673,290 798,185 923,290 798,415" fill="url(#plaid)" stroke="var(--gold)" stroke-width="4" role="img" aria-label="Photo: woman drilling into a wall"/>
    <polygon points="801,445 896,350 991,445 896,540" fill="url(#plaid)" stroke="var(--gold)" stroke-width="4" role="img" aria-label="Photo: smiling student at a workbench"/>
    <polygon points="474,505 651,330 826,505 651,680" fill="url(#warmB)" stroke="var(--gold)" stroke-width="5" role="img" aria-label="Photo: student in safety glasses drilling wood"/>
    <polygon points="311,435 406,330 516,435 406,545" fill="url(#warmB)" stroke="var(--teal)" stroke-width="4" role="img" aria-label="Photo: woman marking a board with a pencil"/>
    <polygon points="114,445 223,338 331,445 223,553" fill="url(#plaid)" stroke="var(--teal)" stroke-width="4" role="img" aria-label="Photo: woman holding a power drill"/>
  </svg>

  <div class="brand" style="left:362px">
    <span class="brand__mark"></span>
    <div><div class="brand__name">FixWise Workshop</div><div class="brand__tag">Build every room with confidence.</div></div>
  </div>

  <h1 class="headline" style="left:34px;top:62px">LEARN TO RENO</h1>
  <p class="subhead" style="left:34px;top:103px;font-size:25px">Hands-on training</p>

  <div class="topic" style="left:52px;top:148px"><svg viewBox="0 0 14 14"><rect x="1" y="1" width="12" height="12" fill="none" stroke="var(--gold)" stroke-width="1.6"/><path d="M3 7l4-4 4 4M4 7v5M10 7v5M4 10h6" fill="none" stroke="var(--gold)" stroke-width="1.3"/></svg>Framing</div>
  <div class="topic" style="left:158px;top:146px"><svg viewBox="0 0 14 14"><rect x="1" y="1" width="12" height="12" fill="none" stroke="var(--gold)" stroke-width="1.6"/><path d="M4 4v4h6v3" fill="none" stroke="var(--gold)" stroke-width="1.5"/></svg>Plumbing</div>
  <div class="topic" style="left:93px;top:171px"><svg viewBox="0 0 14 14"><rect x="1" y="1" width="12" height="12" fill="none" stroke="var(--gold)" stroke-width="1.6"/><path d="M3 10h8M3 8h8" stroke="var(--gold)" stroke-width="1.2"/></svg>Base Boards</div>
  <div class="topic" style="left:83px;top:195px"><svg viewBox="0 0 14 14"><rect x="1" y="1" width="12" height="12" fill="none" stroke="var(--gold)" stroke-width="1.6"/><path d="M1 5h12M1 9h12M5 1v4M9 5v4M5 9v4" stroke="var(--gold)" stroke-width="1.2"/></svg>Feature Walls</div>

  <div class="web" style="left:66px;top:372px">www.fixwiseworkshop-example.com</div>
</section>

</body>
</html>
```